Business Card for a Mortgage Agent (myself)

I need a business card for my new job as Mortgage Agent. The Broker's logo is to be on the card as well as the brokerage License number. Not sure if to include a photo or not. Info to be on card.
Dante Roux
Mortgage Agent
Lic # M47105386
Cell: 905-614-2753
Email: danterouxk.ma@fennmail.com
Web: www.karlvostermortgages.com
TPW Brokerage Lic. # 73918

```html
<!DOCTYPE html>
<html lang="en">
<head>
<meta charset="UTF-8">
<title>Dante Roux – Mortgage Agent Business Card</title>
<link href="https://fonts.googleapis.com/css2?family=Montserrat:wght@400;500;700&display=swap" rel="stylesheet">
<style>
  :root {
    --backdrop: #333232;
    --card-white: #ffffff;
    --brand-blue: #134a8c;
    --brand-yellow: #fdca0a;
    --text-light: #ffffff;
  }
  * { margin: 0; padding: 0; box-sizing: border-box; }
  html, body {
    width: 1200px;
    height: 984px;
    overflow: hidden;
    background: var(--backdrop);
    font-family: "Montserrat", sans-serif;
  }
  .sheet {
    position: relative;
    width: 1200px;
    height: 984px;
  }
  .card {
    position: absolute;
    left: 220px;
    width: 760px;
    height: 434px;
    background: var(--card-white);
    overflow: hidden;
  }
  .card--front { top: 38px; }
  .card--back { top: 512px; display: flex; }

  /* Front */
  .brand {
    position: absolute;
    left: 0; right: 0; top: 0; bottom: 0;
    display: flex;
    flex-direction: column;
    align-items: center;
    justify-content: center;
    gap: 14px;
  }
  .brand__lockup {
    display: flex;
    align-items: center;
    gap: 16px;
  }
  .brand__square {
    width: 44px;
    height: 44px;
    background: var(--brand-yellow);
  }
  .brand__name {
    color: var(--brand-blue);
    font-weight: 700;
    font-size: 38px;
    letter-spacing: 2px;
    text-transform: uppercase;
  }
  .brand__license {
    align-self: flex-end;
    margin-right: 160px;
    color: var(--brand-blue);
    font-weight: 500;
    font-size: 16px;
  }

  /* Back */
  .back__brand {
    width: 270px;
    height: 100%;
    display: flex;
    flex-direction: column;
    align-items: center;
    justify-content: center;
    gap: 14px;
  }
  .back__brand .brand__square { width: 34px; height: 34px; }
  .back__brand .brand__name {
    font-size: 21px;
    letter-spacing: 1px;
    text-align: center;
  }
  .back__brand .brand__license {
    align-self: center;
    margin: 0;
    font-size: 13px;
  }
  .back__panel {
    flex: 1;
    background: var(--brand-blue);
    color: var(--text-light);
    padding: 76px 30px 0 60px;
  }
  .agent__name {
    font-weight: 700;
    font-size: 32px;
    letter-spacing: 0.5px;
    text-transform: uppercase;
    line-height: 1.05;
  }
  .agent__title {
    font-weight: 500;
    font-size: 22px;
    margin-bottom: 20px;
  }
  .agent__licenses p {
    font-size: 20px;
    font-weight: 500;
    line-height: 1.45;
  }
  .contact {
    list-style: none;
    margin-top: 24px;
  }
  .contact__item {
    display: flex;
    align-items: center;
    gap: 14px;
    font-size: 19px;
    font-weight: 500;
    line-height: 1.65;
  }
  .contact__icon {
    width: 20px;
    height: 20px;
    flex-shrink: 0;
  }
</style>
</head>
<body>
<main class="sheet">

  <section class="card card--front" aria-label="Card front">
    <div class="brand">
      <div class="brand__lockup">
        <span class="brand__square"></span>
        <span class="brand__name">Tall Pine Wealth</span>
      </div>
      <span class="brand__license">License #73918</span>
    </div>
  </section>

  <section class="card card--back" aria-label="Card back">
    <div class="back__brand">
      <span class="brand__square"></span>
      <span class="brand__name">Tall Pine Wealth</span>
      <span class="brand__license">License #73918</span>
    </div>

    <div class="back__panel">
      <h1 class="agent__name">Dante Roux</h1>
      <p class="agent__title">Mortgage Agent</p>
      <div class="agent__licenses">
        <p>Lic # M47105386</p>
        <p>TPW Brokerage Lic. # 73918</p>
      </div>
      <ul class="contact">
        <li class="contact__item">
          <svg class="contact__icon" viewBox="0 0 24 24" aria-hidden="true">
            <path fill="#fff" d="M6.6 10.8a15.1 15.1 0 0 0 6.6 6.6l2.2-2.2c.3-.3.7-.4 1-.2 1.1.4 2.3.6 3.6.6.6 0 1 .4 1 1V20c0 .6-.4 1-1 1A17 17 0 0 1 3 4c0-.6.4-1 1-1h3.5c.6 0 1 .4 1 1 0 1.3.2 2.5.6 3.6.1.3 0 .7-.2 1z"/>
          </svg>
          905-614-2753
        </li>
        <li class="contact__item">
          <svg class="contact__icon" viewBox="0 0 24 24" aria-hidden="true">
            <rect x="2" y="5" width="20" height="14" fill="#fff"/>
            <path d="M2 5l10 8 10-8" fill="none" stroke="#134a8c" stroke-width="1.6"/>
          </svg>
          danterouxk.ma@fennmail.com
        </li>
        <li class="contact__item">
          <svg class="contact__icon" viewBox="0 0 24 24" aria-hidden="true">
            <circle cx="12" cy="12" r="10" fill="none" stroke="#fff" stroke-width="2"/>
            <ellipse cx="12" cy="12" rx="4" ry="10" fill="none" stroke="#fff" stroke-width="1.6"/>
            <path d="M2 12h20" stroke="#fff" stroke-width="1.6"/>
          </svg>
          www.karlvostermortgages.com
        </li>
      </ul>
    </div>
  </section>

</main>
</body>
</html>
```